OpenLeaf app needs an improved design

OpenLeaf makes available books that have been banned in certain countries. The current version of the app is available for download here: https://apps.vendrix-market.example/details?id=org.brightmoss.openleaf

At the moment, the app is available only in Chinese. Books are made available within the app, in text or audio format. Books can be downloaded for offline use. We created the app as a way to circumvent the intense censorship that is placed on book distribution inside China. The app is designed in such a way that the authorities are not able to censor the app, thus users in China are able to download the app, read content and receive updates to the app. So far over 100,000 people have used the app. Books are made available to the users for free and the app is also free to download.

We have used a similar anti-censorship strategy in a number of other apps, all with equally successful outcomes.

The app is only available on Android. While many Chinese purchase high end Android devices, Android is also the operating system of choice for new internet users in China. Oftentimes, the first time a user accesses the internet will be through an inexpensive Android smartphone.

This is very much a content driven app, with limited functionality but very visual. We need to optimize the app so that it is suitable for reading long texts. While we make available banned books through the app itself, our users are primarily avid readers - they are not likely to be netizens who wanted to download a book app just because it contains banned books. They will be readers who are interested in reading and exploring new books that are not normally available to them.

The app should have similar functionality to an e-reader, like a Pagette, however it needs to be optimized for smaller screens. Apps like Scrollnest present content in an easy to read format.

Target Market(s)

Our current end users are Chinese who are professionals and have an interest in reading. They are likely between the ages of 18-50. We try to make the app as easy and intuitive as possible. Even though there are over 700 million people online in China, another 600 million of them will come online soon. We want experienced internet and technology users to easily find the content they are looking for and we want new internet and technology users to be able to easily use the app. Our users mainly use the app in the comfort of their own home - as they would read an e-book (Pagette) or in a quiet cafe.

Industry/Entity Type

Book Publisher

Font styles to use
Serif

Colors

Designer to choose colors to be used in the design.

Requirements
Must have
• Our current challenges include:
• - We want to promote new books as well as popular books (and potentially other categories) and allow users to browse more books in that category.
• - Allow users to search.
• - For each book, we need an indication whether it is an audio book or a text book.
• - For each book, we need an indication whether the book has already been downloaded.
• Our current audio book challenges include:
• - Show book cover.
• - Include all standard audio playback functions (pause, play, next chapter etc).
• - Audio books can play in the background. When the user leaves this view, the app needs to indicate that an audio book is playing in the background, and show the user how to return to this interface (to pause playback, etc).
• Our current text book challenges include:
• - Show name of book.
• - Maximize use of screen (since it may be hard to read on a small device).
• - Allow user to easily navigate (next page, any page number etc).

```html
<!DOCTYPE html>
<html lang="en">
<head>
<meta charset="utf-8">
<title>OpenLeaf – Downloading</title>
<link rel="stylesheet" href="https://fonts.googleapis.com/css2?family=Roboto:wght@300;400;500;700&display=swap">
<style>
  :root {
    --brand: #2ea3cb;
    --brand-dark: #1f86aa;
    --page: #eef3f5;
    --field: #f7fafb;
    --ink: #1e2a30;
    --muted: #6f7c83;
    --rule: #2a95bd;
    --scrim: rgba(16, 26, 31, 0.64);
    --modal: #ffffff;
    --modal-ink: #20282c;
    --track: #dadcdd;
    --accent: #12b1e6;
    --icon-line: #8d9296;
  }
  * { box-sizing: border-box; margin: 0; padding: 0; }
  html, body { width: 675px; height: 1200px; overflow: hidden; }
  body {
    position: relative;
    background: var(--page);
    font-family: "Roboto", "Helvetica Neue", Arial, sans-serif;
    color: var(--ink);
  }
  .status-bar {
    position: absolute; left: 0; top: 0; width: 675px; height: 36px;
    background: var(--brand); color: #fff;
    display: flex; align-items: center; padding: 0 12px;
    font-size: 18px;
  }
  .status-bar .signal { display: flex; gap: 2px; margin-right: 6px; }
  .status-bar .signal span { width: 9px; height: 9px; border-radius: 50%; background: #fff; }
  .status-bar .time { position: absolute; left: 0; right: 0; text-align: center; font-weight: 500; }
  .status-bar .battery {
    position: absolute; right: 14px; top: 11px; width: 36px; height: 15px;
    border: 1.5px solid #fff; border-radius: 3px; padding: 1.5px;
  }
  .status-bar .battery::before { content: ""; display: block; width: 100%; height: 100%; background: #fff; border-radius: 1px; }
  .app-header {
    position: absolute; left: 0; top: 36px; width: 675px; height: 79px;
    background: var(--brand);
    display: flex; align-items: center; justify-content: center;
    color: #fff; font-size: 30px; font-weight: 500;
  }
  .app-header .menu { position: absolute; left: 19px; top: 26px; width: 32px; }
  .search {
    position: absolute; left: 19px; top: 140px; width: 636px; height: 66px;
    background: var(--field); display: flex;
  }
  .search .query { flex: 1; padding-left: 37px; line-height: 66px; font-size: 23px; color: var(--muted); }
  .search .go { width: 78px; background: var(--brand); display: flex; align-items: center; justify-content: center; }
  .shelf { position: absolute; left: 0; width: 675px; }
  .shelf-title {
    position: absolute; left: 21px; top: 0; font-size: 26px; font-weight: 700; color: var(--ink);
  }
  .shelf-more { position: absolute; right: 12px; top: 4px; }
  .shelf-row { position: absolute; left: 0; }
  .book { position: absolute; width: 149px; }
  .cover { width: 149px; height: 184px; }
  .book-action { margin-top: 8px; font-size: 18px; color: var(--muted); }
  .shelf-rule { position: absolute; left: 0; width: 675px; height: 3px; background: var(--rule); }
  .shelf-rule .knob {
    position: absolute; top: -7px; width: 17px; height: 17px; border-radius: 50%;
    background: var(--page); border: 3px solid var(--rule);
  }
  .scrim { position: absolute; inset: 0; background: var(--scrim); }
  .download-dialog {
    position: absolute; left: 86px; top: 256px; width: 503px; height: 492px;
    background: var(--modal); color: var(--modal-ink); text-align: center;
  }
  .download-dialog .close { position: absolute; left: 457px; top: 17px; }
  .download-dialog .hourglass { position: absolute; left: 210px; top: 76px; }
  .download-dialog .percent { position: absolute; left: 0; right: 0; top: 200px; font-size: 21px; }
  .progress {
    position: absolute; left: 71px; top: 241px; width: 360px; height: 6px;
    background: var(--track); border-radius: 3px; overflow: hidden;
  }
  .progress .fill { width: 76%; height: 100%; background: var(--accent); border-radius: 3px; }
  .download-dialog .status { position: absolute; left: 0; right: 0; top: 274px; font-size: 37px; font-weight: 400; }
  .download-dialog .author { position: absolute; left: 0; right: 0; top: 327px; font-size: 20px; letter-spacing: 0.5px; }
  .download-dialog .note {
    position: absolute; left: 40px; right: 40px; top: 370px; font-size: 23px; line-height: 32px; font-weight: 400;
  }
</style>
</head>
<body>
  <div class="status-bar">
    <div class="signal"><span></span><span></span><span></span><span></span><span></span></div>
    <span>Carrier</span>
    <span class="time">13:37</span>
    <div class="battery"></div>
  </div>

  <header class="app-header">
    <svg class="menu" width="32" height="24" viewBox="0 0 32 24"><rect y="0" width="32" height="4" fill="#fff"/><rect y="10" width="32" height="4" fill="#fff"/><rect y="20" width="32" height="4" fill="#fff"/></svg>
    Free Book
  </header>

  <div class="search">
    <div class="query">Fiction Stories</div>
    <div class="go">
      <svg width="36" height="36" viewBox="0 0 36 36"><circle cx="15" cy="15" r="10" fill="none" stroke="#fff" stroke-width="4"/><line x1="22" y1="22" x2="32" y2="32" stroke="#fff" stroke-width="5" stroke-linecap="round"/></svg>
    </div>
  </div>

  <section class="shelf" style="top:231px">
    <h2 class="shelf-title">Function Stories</h2>
    <svg class="shelf-more" width="16" height="26" viewBox="0 0 16 26"><polyline points="3,3 13,13 3,23" fill="none" stroke="#9aa3a7" stroke-width="3"/></svg>
    <div class="book" style="left:19px;top:59px"><div class="cover" role="img" aria-label="Cover of a classic story anthology" style="background:linear-gradient(160deg,#6aa37a,#c9856c)"></div><div class="book-action">Download</div></div>
    <div class="book" style="left:181px;top:59px"><div class="cover" role="img" aria-label="Book cover" style="background:linear-gradient(160deg,#8a9aa4,#4e5e66)"></div><div class="book-action">View</div></div>
    <div class="book" style="left:342px;top:59px"><div class="cover" role="img" aria-label="Book cover" style="background:linear-gradient(160deg,#b7a58d,#6d5c4a)"></div><div class="book-action">Download</div></div>
    <div class="book" style="left:504px;top:59px"><div class="cover" role="img" aria-label="Cover of a dark thriller" style="background:linear-gradient(160deg,#b9a698,#5e4a40)"></div><div class="book-action">Download</div></div>
    <div class="shelf-rule" style="top:287px"><span class="knob" style="left:29px"></span></div>
  </section>

  <section class="shelf" style="top:550px">
    <h2 class="shelf-title">Religious</h2>
    <svg class="shelf-more" width="16" height="26" viewBox="0 0 16 26"><polyline points="3,3 13,13 3,23" fill="none" stroke="#9aa3a7" stroke-width="3"/></svg>
    <div class="book" style="left:19px;top:70px"><div class="cover" role="img" aria-label="Cover of a spy thriller with a bird over a pale sky" style="background:linear-gradient(170deg,#f1f4f4,#cfd9da 70%,#2fb6d0)"></div><div class="book-action">Download</div></div>
    <div class="book" style="left:181px;top:70px"><div class="cover" role="img" aria-label="Cover of a classic horror anthology" style="background:linear-gradient(170deg,#6a6252,#2c2a28)"></div><div class="book-action">Download</div></div>
    <div class="book" style="left:342px;top:70px"><div class="cover" role="img" aria-label="Cover of a novel with a figure in a dark dress" style="background:linear-gradient(170deg,#e8dcc4,#3b3430)"></div><div class="book-action">Download</div></div>
    <div class="book" style="left:504px;top:70px"><div class="cover" role="img" aria-label="Cover of a thriller with a running figure" style="background:linear-gradient(170deg,#9fb9c4,#5e7b64)"></div><div class="book-action">View</div></div>
    <div class="shelf-rule" style="top:298px"><span class="knob" style="left:357px"></span></div>
  </section>

  <section class="shelf" style="top:884px">
    <h2 class="shelf-title">Romantic</h2>
    <svg class="shelf-more" width="16" height="26" viewBox="0 0 16 26"><polyline points="3,3 13,13 3,23" fill="none" stroke="#9aa3a7" stroke-width="3"/></svg>
    <div class="book" style="left:19px;top:73px"><div class="cover" role="img" aria-label="Cover of an audio novel with a hooded figure" style="background:linear-gradient(170deg,#7f8f8c,#2f3a34 60%,#9a8a3a)"></div><div class="book-action">View</div></div>
    <div class="book" style="left:181px;top:73px"><div class="cover" role="img" aria-label="Cover of a western with a stormy sky over a gallows" style="background:linear-gradient(170deg,#8c9394,#c9cbc6 60%,#a6a39a)"></div><div class="book-action">Download</div></div>
    <div class="book" style="left:342px;top:73px"><div class="cover" role="img" aria-label="Cover of a thriller with bold gold title lettering" style="background:linear-gradient(170deg,#4c5557,#262c2d)"></div><div class="book-action">View</div></div>
    <div class="book" style="left:504px;top:73px"><div class="cover" role="img" aria-label="Cover of a thriller with an armoured vehicle" style="background:linear-gradient(170deg,#e6e9d2,#cfd2a5 60%,#8a8b60)"></div><div class="book-action">Download</div></div>
    <div class="shelf-rule" style="top:302px"><span class="knob" style="left:157px"></span></div>
  </section>

  <div class="scrim"></div>

  <div class="download-dialog" role="dialog" aria-label="Download progress">
    <svg class="close" width="26" height="26" viewBox="0 0 26 26"><line x1="2" y1="2" x2="24" y2="24" stroke="#8a9094" stroke-width="2.4"/><line x1="24" y1="2" x2="2" y2="24" stroke="#8a9094" stroke-width="2.4"/></svg>
    <svg class="hourglass" width="83" height="95" viewBox="0 0 83 95">
      <path d="M4 3 H79 C79 30 50 38 50 47.5 C50 57 79 65 79 92 H4 C4 65 33 57 33 47.5 C33 38 4 30 4 3 Z" fill="none" stroke="var(--icon-line)" stroke-width="3.5" stroke-linejoin="round"/>
      <path d="M11 10 H72 C70 26 54 32 41.5 38 C29 32 13 26 11 10 Z" fill="var(--accent)"/>
      <path d="M41.5 58 C56 63 70 72 72 86 H11 C13 72 27 63 41.5 58 Z" fill="var(--accent)"/>
    </svg>
    <div class="percent">87%</div>
    <div class="progress"><div class="fill"></div></div>
    <div class="status">Downloding</div>
    <div class="author">HOLLIS MARBURY’S</div>
    <p class="note">it will take some time to download the book</p>
  </div>
</body>
</html>
```